Bottom fuel dispenser panel

Design the fuel dispenser lower panel graphics based on our brand “tandrel”
I will attach the brand logo and picture of the dispenser along with some other examples of other brands portraying their logos.

Target Market(s)

Petrol pump consumers

Industry/Entity Type

Oil and gas retailer

Requirements
Must have
• Theme that matches our brand
Nice to have
• Please refer to the image of the gas station in tandrel branded photos. Size of the bottom panel is 28” by 45”.
Should not have
• Too many colors

```html
<!DOCTYPE html>
<html lang="en">
<head>
<meta charset="utf-8">
<title>tandrel — fuel dispenser lower panels</title>
<link rel="stylesheet" href="https://fonts.googleapis.com/css2?family=Open+Sans:wght@800&display=swap">
<style>
  :root {
    --brand-green: #93ff0a;
    --brand-black: #030303;
    --paper: #ffffff;
    --trim: #b5b5b5;
  }
  html, body {
    margin: 0;
    padding: 0;
    width: 1200px;
    height: 1200px;
    overflow: hidden;
    background: var(--paper);
  }
  .artboard {
    display: block;
    width: 1200px;
    height: 1200px;
  }
  .panel-frame { fill: var(--paper); stroke: var(--trim); stroke-width: 1.5; }
  .band-green { fill: var(--brand-green); }
  .band-black { fill: var(--brand-black); }
  .brand-name {
    font-family: "Open Sans", sans-serif;
    font-weight: 800;
    fill: var(--brand-black);
    letter-spacing: -2px;
  }
</style>
</head>
<body>
<svg class="artboard" viewBox="0 0 1932 1932" xmlns="http://www.w3.org/2000/svg" role="img" aria-label="Two tandrel dispenser lower panel designs">
  <!-- Panel option one -->
  <g class="panel panel--stripe">
    <rect class="panel-frame" x="345" y="113" width="1242" height="772"/>
    <rect class="band-black" x="345" y="113" width="78" height="772"/>
    <polygon class="band-green" points="423,113 641,113 641,500 1263,113 1587,113 1587,162 423,885"/>
    <polygon class="band-black" points="641,113 719,113 719,362 1119,113 1263,113 641,500"/>
    <polygon class="band-black" points="423,885 1587,162 1587,251 567,885"/>
    <text class="brand-name" x="1545" y="832" text-anchor="end" font-size="160" textLength="500" lengthAdjust="spacingAndGlyphs">tandrel</text>
    <rect class="panel-frame" x="345" y="113" width="1242" height="772" fill="none" style="fill:none"/>
  </g>

  <!-- Panel option two -->
  <g class="panel panel--open">
    <rect class="panel-frame" x="345" y="1046" width="1242" height="772"/>
    <polygon class="band-green" points="345,1046 563,1046 563,1433 1185,1046 1587,1046 345,1818"/>
    <polygon class="band-black" points="623,1046 701,1046 701,1184 923,1046 1067,1046 623,1322"/>
    <text class="brand-name" x="1535" y="1750" text-anchor="end" font-size="205" textLength="640" lengthAdjust="spacingAndGlyphs">tandrel</text>
    <rect class="panel-frame" x="345" y="1046" width="1242" height="772" style="fill:none"/>
  </g>
</svg>
</body>
</html>
```